Query A Legal Mentor

We need banner ad design for a new company that supplies supplemental study materials for law students. All content on the site is completely free and we assist law students with supplemental materials for daily course work and for preparing for final exams. The site provides free: Q&A - all answers provided by law professors, Audio Lectures on the most important law school topics, Outline Overviews, Charts and Notes of difficult and confusing law school topics, mini essays with answers for exam preparation.
Updates

ads need to be in the following sizes: 728x90, 160x600, 300x250, 468x60, 120x240

Reason: the ad target market are 'professional students' so it cannot look childish in design. The design must be professional looking.

Target Market(s)

Law Students .. review the QueryALegalMentor.example site

Industry/Entity Type

School

Requirements
Must have
• The word 'Free' must be very prominent throughout the ads
Nice to have
• Try to include 'all of the free items' that are included that the user receives once the register for free for the site. Also the ads may include animation so that each free item the user receives may be able to stand out better.

```html
<!DOCTYPE html>
<html lang="en">
<head>
<meta charset="utf-8">
<title>Query A Legal Mentor – Banner Set</title>
<link rel="stylesheet" href="https://fonts.googleapis.com/css2?family=Arimo:wght@400;700&family=Archivo+Narrow:wght@700&display=swap">
<style>
  :root {
    --stage: #ece6de;
    --brand-blue: #1183c4;
    --free-green: #2bef2b;
    --tick-green: #2ee02e;
    --white: #ffffff;
    --photo-dark: #3a1d0c;
    --photo-mid: #8a4a1c;
    --photo-light: #d9b07a;
  }
  * { box-sizing: border-box; margin: 0; padding: 0; }
  html, body { width: 1200px; height: 900px; overflow: hidden; background: var(--stage); }
  .stage { position: relative; width: 1024px; height: 768px; transform: scale(1.171875); transform-origin: 0 0; }

  .banner { position: absolute; background: var(--brand-blue); overflow: hidden; font-family: "Arimo", Arial, sans-serif; color: var(--white); font-weight: 700; }
  .photo { position: absolute; background: linear-gradient(135deg, var(--photo-dark) 0%, var(--photo-mid) 45%, var(--photo-light) 80%, #f3e3c6 100%); border: 0 solid var(--white); }
  .notch { position: absolute; width: 0; height: 0; border-left: 9px solid transparent; border-right: 9px solid transparent; border-bottom: 10px solid var(--white); }
  .abs { position: absolute; }
  .free { font-family: "Archivo Narrow", "Arial Narrow", sans-serif; color: var(--free-green); line-height: 1; text-align: center; transform: scaleY(1.15); transform-origin: top; }
  .tagline { text-align: center; line-height: 1.2; }
  .brand { text-align: center; white-space: nowrap; line-height: 1.1; }
  .perks { list-style: none; }
  .perks li { display: flex; align-items: center; white-space: nowrap; }
  .tick { flex: none; fill: none; stroke: var(--tick-green); stroke-width: 2.6; stroke-linecap: round; stroke-linejoin: round; }
  .enroll { position: absolute; background: var(--free-green); border-radius: 8px; display: flex; align-items: center; justify-content: center; white-space: nowrap; }
  .url { text-align: center; white-space: nowrap; letter-spacing: -0.1px; }

  /* 728 x 90 leaderboard */
  .leaderboard { left: 149px; top: 40px; width: 728px; height: 89px; }
  .leaderboard .photo { left: 0; top: -10px; width: 205px; height: 110px; border-right-width: 6px; border-radius: 0 60px 60px 0 / 0 55px 55px 0; }
  .leaderboard .free { left: 212px; top: 2px; width: 120px; font-size: 50px; }
  .leaderboard .tagline { left: 205px; top: 56px; width: 135px; font-size: 12.5px; }
  .leaderboard .perks { left: 372px; top: 2px; font-size: 15px; }
  .leaderboard .perks li { height: 21px; gap: 4px; }
  .leaderboard .tick { width: 16px; height: 16px; }
  .leaderboard .brand { left: 562px; top: 10px; width: 166px; font-size: 14px; }
  .leaderboard .enroll { left: 572px; top: 33px; width: 150px; height: 36px; font-size: 17px; }
  .leaderboard .url { left: 550px; top: 75px; width: 174px; font-size: 10.2px; }

  /* 468 x 60 banner */
  .full-banner { left: 292px; top: 197px; width: 468px; height: 60px; }
  .full-banner .photo { left: 0; top: -8px; width: 132px; height: 76px; border-right-width: 4px; border-radius: 0 40px 40px 0 / 0 38px 38px 0; }
  .full-banner .free { left: 136px; top: 2px; width: 76px; font-size: 32px; }
  .full-banner .tagline { left: 130px; top: 36px; width: 90px; font-size: 8.5px; }
  .full-banner .perks { left: 240px; top: 1px; font-size: 10px; }
  .full-banner .perks li { height: 14px; gap: 3px; }
  .full-banner .tick { width: 10px; height: 10px; }
  .full-banner .brand { left: 356px; top: 6px; width: 112px; font-size: 9.5px; }
  .full-banner .enroll { left: 367px; top: 22px; width: 91px; height: 24px; font-size: 11px; border-radius: 6px; }
  .full-banner .url { left: 352px; top: 49px; width: 114px; font-size: 6.9px; }

  /* 300 x 250 medium rectangle */
  .rectangle { left: 213px; top: 349px; width: 300px; height: 250px; }
  .rectangle .photo { left: -10px; top: 0; width: 182px; height: 182px; border-right-width: 6px; border-bottom-width: 6px; border-radius: 0 0 100% 0 / 0 0 100% 0; }
  .rectangle .notch { left: 42px; top: 166px; }
  .rectangle .brand { left: 172px; top: 14px; width: 128px; font-size: 11px; }
  .rectangle .free { left: 188px; top: 44px; width: 96px; font-size: 44px; }
  .rectangle .tagline { left: 172px; top: 95px; width: 128px; font-size: 12.5px; }
  .rectangle .perks { left: 150px; top: 130px; font-size: 13.5px; }
  .rectangle .perks li { height: 19px; gap: 4px; }
  .rectangle .tick { width: 14px; height: 14px; }
  .rectangle .enroll { left: 7px; top: 200px; width: 126px; height: 32px; font-size: 15px; }
  .rectangle .url { left: 2px; top: 237px; width: 144px; font-size: 8.8px; }

  /* 120 x 240 vertical banner */
  .vertical { left: 581px; top: 355px; width: 120px; height: 240px; }
  .vertical .photo { left: -10px; top: -10px; width: 140px; height: 72px; border-bottom-width: 4px; border-radius: 0 0 50% 50% / 0 0 24px 24px; }
  .vertical .notch { left: 52px; top: 53px; border-left-width: 6px; border-right-width: 6px; border-bottom-width: 7px; }
  .vertical .brand { left: 0; top: 80px; width: 120px; font-size: 9.5px; }
  .vertical .free { left: 30px; top: 95px; width: 60px; font-size: 22px; }
  .vertical .tagline { left: 0; top: 121px; width: 120px; font-size: 8.5px; }
  .vertical .perks { left: 4px; top: 144px; font-size: 8.5px; }
  .vertical .perks li { height: 14px; gap: 2px; }
  .vertical .tick { width: 9px; height: 9px; }
  .vertical .enroll { left: 12px; top: 206px; width: 96px; height: 28px; font-size: 10.5px; border-radius: 7px; }

  /* 160 x 600 wide skyscraper */
  .skyscraper { left: 846px; top: 151px; width: 160px; height: 600px; }
  .skyscraper .photo { left: -10px; top: -10px; width: 180px; height: 245px; border-bottom-width: 6px; border-radius: 0 0 50% 50% / 0 0 40px 40px; }
  .skyscraper .notch { left: 72px; top: 226px; }
  .skyscraper .brand { left: 0; top: 276px; width: 160px; font-size: 12.5px; }
  .skyscraper .free { left: 25px; top: 300px; width: 110px; font-size: 50px; }
  .skyscraper .tagline { left: 0; top: 355px; width: 160px; font-size: 13px; }
  .skyscraper .perks { left: 3px; top: 393px; font-size: 15px; }
  .skyscraper .perks li { height: 21px; gap: 3px; }
  .skyscraper .tick { width: 16px; height: 16px; }
  .skyscraper .enroll { left: 10px; top: 537px; width: 142px; height: 37px; font-size: 16.5px; }
  .skyscraper .url { left: 0; top: 582px; width: 160px; font-size: 9.4px; }
</style>
</head>
<body>
<main class="stage">

  <section class="banner leaderboard" aria-label="728 by 90 banner">
    <div class="photo" role="img" aria-label="Photo of a laptop and an open law book before shelves of old books"></div>
    <div class="abs free">FREE</div>
    <p class="abs tagline">Law Supplemental<br>Materials</p>
    <ul class="abs perks">
      <li><svg class="tick" viewBox="0 0 12 12"><path d="M1.5 6.5l3 3.5L10.5 1.5"/></svg>Q &amp; A</li>
      <li><svg class="tick" viewBox="0 0 12 12"><path d="M1.5 6.5l3 3.5L10.5 1.5"/></svg>Topic Videos</li>
      <li><svg class="tick" viewBox="0 0 12 12"><path d="M1.5 6.5l3 3.5L10.5 1.5"/></svg>Audio lectures</li>
      <li><svg class="tick" viewBox="0 0 12 12"><path d="M1.5 6.5l3 3.5L10.5 1.5"/></svg>Charts and Notes</li>
    </ul>
    <p class="abs brand">Query A Legal Mentor</p>
    <div class="enroll">Free Enrollment</div>
    <p class="abs url">www.queryalegalmentor.example</p>
  </section>

  <section class="banner full-banner" aria-label="468 by 60 banner">
    <div class="photo" role="img" aria-label="Photo of a laptop and an open law book before shelves of old books"></div>
    <div class="abs free">FREE</div>
    <p class="abs tagline">Law Supplemental<br>Materials</p>
    <ul class="abs perks">
      <li><svg class="tick" viewBox="0 0 12 12"><path d="M1.5 6.5l3 3.5L10.5 1.5"/></svg>Q &amp; A</li>
      <li><svg class="tick" viewBox="0 0 12 12"><path d="M1.5 6.5l3 3.5L10.5 1.5"/></svg>Topic Videos</li>
      <li><svg class="tick" viewBox="0 0 12 12"><path d="M1.5 6.5l3 3.5L10.5 1.5"/></svg>Audio lectures</li>
      <li><svg class="tick" viewBox="0 0 12 12"><path d="M1.5 6.5l3 3.5L10.5 1.5"/></svg>Charts and Notes</li>
    </ul>
    <p class="abs brand">Query A Legal Mentor</p>
    <div class="enroll">Free Enrollment</div>
    <p class="abs url">www.queryalegalmentor.example</p>
  </section>

  <section class="banner rectangle" aria-label="300 by 250 banner">
    <div class="photo" role="img" aria-label="Photo of a laptop and an open law book before shelves of old books"></div>
    <div class="notch"></div>
    <p class="abs brand">Query A Legal Mentor</p>
    <div class="abs free">FREE</div>
    <p class="abs tagline">Law Supplemental<br>Materials</p>
    <ul class="abs perks">
      <li><svg class="tick" viewBox="0 0 12 12"><path d="M1.5 6.5l3 3.5L10.5 1.5"/></svg>Q &amp; A</li>
      <li><svg class="tick" viewBox="0 0 12 12"><path d="M1.5 6.5l3 3.5L10.5 1.5"/></svg>Topic Videos</li>
      <li><svg class="tick" viewBox="0 0 12 12"><path d="M1.5 6.5l3 3.5L10.5 1.5"/></svg>Audio lectures</li>
      <li><svg class="tick" viewBox="0 0 12 12"><path d="M1.5 6.5l3 3.5L10.5 1.5"/></svg>Outline Overviews</li>
      <li><svg class="tick" viewBox="0 0 12 12"><path d="M1.5 6.5l3 3.5L10.5 1.5"/></svg>Charts and Notes</li>
      <li><svg class="tick" viewBox="0 0 12 12"><path d="M1.5 6.5l3 3.5L10.5 1.5"/></svg>Mini Essays</li>
    </ul>
    <div class="enroll">Free Enrollment</div>
    <p class="abs url">www.queryalegalmentor.example</p>
  </section>

  <section class="banner vertical" aria-label="120 by 240 banner">
    <div class="photo" role="img" aria-label="Photo of a laptop and an open law book before shelves of old books"></div>
    <div class="notch"></div>
    <p class="abs brand">Query A Legal Mentor</p>
    <div class="abs free">FREE</div>
    <p class="abs tagline">Law Supplemental<br>Materials</p>
    <ul class="abs perks">
      <li><svg class="tick" viewBox="0 0 12 12"><path d="M1.5 6.5l3 3.5L10.5 1.5"/></svg>Q &amp; A</li>
      <li><svg class="tick" viewBox="0 0 12 12"><path d="M1.5 6.5l3 3.5L10.5 1.5"/></svg>Topic Videos</li>
      <li><svg class="tick" viewBox="0 0 12 12"><path d="M1.5 6.5l3 3.5L10.5 1.5"/></svg>Audio lectures</li>
      <li><svg class="tick" viewBox="0 0 12 12"><path d="M1.5 6.5l3 3.5L10.5 1.5"/></svg>Charts and Notes</li>
    </ul>
    <div class="enroll">Free Enrollment</div>
  </section>

  <section class="banner skyscraper" aria-label="160 by 600 banner">
    <div class="photo" role="img" aria-label="Photo of a desk lamp, laptop and open law book before shelves of old books"></div>
    <div class="notch"></div>
    <p class="abs brand">Query A Legal Mentor</p>
    <div class="abs free">FREE</div>
    <p class="abs tagline">Law Supplemental<br>Materials</p>
    <ul class="abs perks">
      <li><svg class="tick" viewBox="0 0 12 12"><path d="M1.5 6.5l3 3.5L10.5 1.5"/></svg>Q &amp; A</li>
      <li><svg class="tick" viewBox="0 0 12 12"><path d="M1.5 6.5l3 3.5L10.5 1.5"/></svg>Topic Videos</li>
      <li><svg class="tick" viewBox="0 0 12 12"><path d="M1.5 6.5l3 3.5L10.5 1.5"/></svg>Audio lectures</li>
      <li><svg class="tick" viewBox="0 0 12 12"><path d="M1.5 6.5l3 3.5L10.5 1.5"/></svg>Outline Overviews</li>
      <li><svg class="tick" viewBox="0 0 12 12"><path d="M1.5 6.5l3 3.5L10.5 1.5"/></svg>Charts and Notes</li>
      <li><svg class="tick" viewBox="0 0 12 12"><path d="M1.5 6.5l3 3.5L10.5 1.5"/></svg>Mini Essays</li>
    </ul>
    <div class="enroll">Free Enrollment</div>
    <p class="abs url">www.queryalegalmentor.example</p>
  </section>

</main>
</body>
</html>
```